2019/20 Season Calendar (This is to be at the top of the calendar as title)

An advertising calendar for our agricultural business to explain our key business attributes and give clients a nice looking calendar to refer to .

Please refer to doc/pdf attachments for text details and ideas. (Our current logo needs to be incorporated - this logo can be altered if need be)

open to professional agriculture aesthetics keeping in line with the companies Green colour scheme (logo)

The calendar is to start at October 2019 - September 2020

97mm x 122mm

Target Market(s)

Agricultural sector (professional)

Industry/Entity Type

Agriculture

Font styles to use
Sans Serif

Colors
abd036
3276b5

Requirements
Must have
• Calender with dates starting october 1st 2019 finishing end of september 2020.
• Must include all public holidays etc for Australia during this time.
• contact details including website :www.brevardholdings.com.au
Nice to have
• In the calendar the months of
• October/ nov /december (be coloured yellow)
• April/May/June (be coloured brown)
• July /aug/september (be coloured green)
• Jan/feb/march (be coloured white)
• Then in the corner of the calendar a key (like a map) to refer to the colours
• [a small square with the colour yellow] (next to the square the following text) Harvesting
• [a small square with the colour brown] (next to the square the following text) Sowing
• [a small square with the colour green] (next to the square the following text) Growing
• [a small square with the colour white] (next to the square the following text) Liming + Fertilising

```html
<!DOCTYPE html>
<html lang="en">
<head>
<meta charset="utf-8">
<title>2019/20 Season Calendar</title>
<link rel="stylesheet" href="https://fonts.googleapis.com/css2?family=Montserrat:wght@400;500;700;800&display=swap">
<style>
:root{
  --bg:#ffffff;
  --brand-green:#abd036;
  --brand-blue:#3276b5;
  --dark-green:#1d8b3c;
  --ink:#2b2b2b;
  --holiday:#e1261c;
  --m-white:#d9d9d9;
  --m-brown:#a0670d;
  --m-green:#4cc94a;
  --m-yellow:#fdf056;
  --legend-bg:#000000;
}
*{margin:0;padding:0;box-sizing:border-box}
html,body{width:1200px;height:960px;overflow:hidden;background:var(--bg)}
body{position:relative;font-family:"Montserrat",Arial,sans-serif;color:var(--ink)}
.calendar{position:absolute;left:184.5px;top:0;width:838px;height:968px;transform:scale(.9917);transform-origin:0 0;background:#fff}
.hero{position:absolute;left:0;top:0;width:838px;height:253px;background:linear-gradient(180deg,#8fa0b4 0%,#b4bfc7 24%,#5c7a3c 30%,#b6c62a 48%,#d7dd22 70%,#a9b92a 100%)}
.hero-band{position:absolute;left:0;top:253px;width:838px;height:12px;background:var(--brand-green)}
.title{position:absolute;left:0;top:12px;width:838px;text-align:center;color:#fff;font-weight:800;font-size:45px;letter-spacing:.5px}
.brand-tab{position:absolute;left:309px;top:180px;width:244px;height:85px;background:var(--brand-green);border-radius:26px 26px 0 0;display:flex;align-items:center;justify-content:center;gap:8px}
.brand-mark{width:14px;height:14px;background:var(--dark-green)}
.brand-name{font-weight:800;font-size:17px;color:var(--dark-green);letter-spacing:.3px}
.month{position:absolute;width:216px;color:var(--ink)}
.month.white{background:var(--m-white)}
.month.brown{background:var(--m-brown);color:#fff}
.month.green{background:var(--m-green)}
.month.yellow{background:var(--m-yellow)}
.month-name{position:absolute;left:25px;top:0;width:167px;height:25px;border-radius:6px;background:var(--brand-blue);color:#fff;font-weight:700;font-size:19px;text-align:center;line-height:25px;letter-spacing:.5px}
.white .month-name{color:#0f1f3a}
.days{position:absolute;left:10px;top:28px;width:198px;display:grid;grid-template-columns:repeat(7,1fr);font-size:14.5px;line-height:19.8px;text-align:center}
.days .hd{font-weight:500}
.days .hol{color:var(--holiday)}
.legend{position:absolute;left:195px;top:895px;width:612px;height:24px;background:var(--legend-bg);display:flex;align-items:center;gap:0;padding-left:25px;color:#fff;font-size:14.5px}
.key{display:flex;align-items:center;margin-right:14px}
.swatch{width:38px;height:14px;margin-right:8px}
.footer-left{position:absolute;left:0;top:924px;width:415px;height:44px;background:var(--brand-green)}
.footer-right{position:absolute;left:418px;top:924px;width:420px;height:44px;background:var(--brand-blue)}
.contact{position:absolute;display:flex;align-items:flex-start;gap:5px;color:#fff;font-size:11.5px;line-height:14px}
.contact svg{flex:none;margin-top:0}
</style>
</head>
<body>
<main class="calendar">
  <div class="hero" role="img" aria-label="Aerial photograph of flowering canola paddocks with scattered gum trees under an overcast sky"></div>
  <div class="hero-band"></div>
  <h1 class="title">2019/20 SEASON CALENDAR</h1>
  <div class="brand-tab"><span class="brand-mark"></span><span class="brand-name">BREVARD HOLDINGS</span></div>

  <section class="month white" style="left:35px;top:283px;height:145px"><div class="month-name">JANUARY</div><div class="days">
    <span class="hd">S</span><span class="hd">M</span><span class="hd">T</span><span class="hd">W</span><span class="hd">T</span><span class="hd">F</span><span class="hd">S</span>
    <span></span><span class="hol">1</span><span>2</span><span>3</span><span>4</span><span>5</span><span>6</span>
    <span>7</span><span>8</span><span>9</span><span>10</span><span>11</span><span>12</span><span>13</span>
    <span>14</span><span>15</span><span>16</span><span>17</span><span>18</span><span>19</span><span>20</span>
    <span>21</span><span>22</span><span>23</span><span>24</span><span>25</span><span class="hol">26</span><span>27</span>
    <span>28</span><span>29</span><span>30</span><span>31</span>
  </div></section>

  <section class="month white" style="left:313px;top:283px;height:145px"><div class="month-name">FEBRUARY</div><div class="days">
    <span class="hd">S</span><span class="hd">M</span><span class="hd">T</span><span class="hd">W</span><span class="hd">T</span><span class="hd">F</span><span class="hd">S</span>
    <span></span><span></span><span></span><span></span><span>1</span><span>2</span><span>3</span>
    <span>4</span><span>5</span><span>6</span><span>7</span><span>8</span><span>9</span><span>10</span>
    <span>11</span><span>12</span><span>13</span><span>14</span><span>15</span><span>16</span><span>17</span>
    <span>18</span><span>19</span><span>20</span><span>21</span><span>22</span><span>23</span><span>24</span>
    <span>25</span><span>26</span><span>27</span><span>28</span>
  </div></section>

  <section class="month white" style="left:591px;top:283px;height:145px"><div class="month-name">MARCH</div><div class="days">
    <span class="hd">S</span><span class="hd">M</span><span class="hd">T</span><span class="hd">W</span><span class="hd">T</span><span class="hd">F</span><span class="hd">S</span>
    <span></span><span></span><span></span><span></span><span>1</span><span>2</span><span>3</span>
    <span>4</span><span class="hol">5</span><span>6</span><span>7</span><span>8</span><span>9</span><span>10</span>
    <span>11</span><span>12</span><span>13</span><span>14</span><span>15</span><span>16</span><span>17</span>
    <span>18</span><span>19</span><span>20</span><span>21</span><span>22</span><span>23</span><span>24</span>
    <span>25</span><span>26</span><span>27</span><span>28</span><span>29</span><span class="hol">30</span><span>31</span>
  </div></section>

  <section class="month brown" style="left:35px;top:438px;height:144px"><div class="month-name">APRIL</div><div class="days">
    <span class="hd">S</span><span class="hd">M</span><span class="hd">T</span><span class="hd">W</span><span class="hd">T</span><span class="hd">F</span><span class="hd">S</span>
    <span>1</span><span class="hol">2</span><span>3</span><span>4</span><span>5</span><span>6</span><span>7</span>
    <span>8</span><span>9</span><span>10</span><span>11</span><span>12</span><span>13</span><span>14</span>
    <span>15</span><span>16</span><span>17</span><span>18</span><span>19</span><span>20</span><span>21</span>
    <span>22</span><span>23</span><span>24</span><span class="hol">25</span><span>26</span><span>27</span><span>28</span>
    <span>29</span><span>30</span>
  </div></section>

  <section class="month brown" style="left:313px;top:438px;height:144px"><div class="month-name">MAY</div><div class="days">
    <span class="hd">S</span><span class="hd">M</span><span class="hd">T</span><span class="hd">W</span><span class="hd">T</span><span class="hd">F</span><span class="hd">S</span>
    <span></span><span></span><span>1</span><span>2</span><span>3</span><span>4</span><span>5</span>
    <span>6</span><span>7</span><span>8</span><span>9</span><span>10</span><span>11</span><span>12</span>
    <span>13</span><span>14</span><span>15</span><span>16</span><span>17</span><span>18</span><span>19</span>
    <span>20</span><span>21</span><span>22</span><span>23</span><span>24</span><span>25</span><span>26</span>
    <span>27</span><span>28</span><span>29</span><span>30</span><span>31</span>
  </div></section>

  <section class="month brown" style="left:591px;top:438px;height:144px"><div class="month-name">JUNE</div><div class="days">
    <span class="hd">S</span><span class="hd">M</span><span class="hd">T</span><span class="hd">W</span><span class="hd">T</span><span class="hd">F</span><span class="hd">S</span>
    <span></span><span></span><span></span><span></span><span></span><span>1</span><span>2</span>
    <span>3</span><span class="hol">4</span><span>5</span><span>6</span><span>7</span><span>8</span><span>9</span>
    <span>10</span><span>11</span><span>12</span><span>13</span><span>14</span><span>15</span><span>16</span>
    <span>17</span><span>18</span><span>19</span><span>20</span><span>21</span><span>22</span><span>23</span>
    <span>24</span><span>25</span><span>26</span><span>27</span><span>28</span><span>29</span><span>30</span>
  </div></section>

  <section class="month green" style="left:35px;top:589px;height:146px"><div class="month-name">JULY</div><div class="days">
    <span class="hd">S</span><span class="hd">M</span><span class="hd">T</span><span class="hd">W</span><span class="hd">T</span><span class="hd">F</span><span class="hd">S</span>
    <span>1</span><span>2</span><span>3</span><span>4</span><span>5</span><span>6</span><span>7</span>
    <span>8</span><span>9</span><span>10</span><span>11</span><span>12</span><span>13</span><span>14</span>
    <span>15</span><span>16</span><span>17</span><span>18</span><span>19</span><span>20</span><span>21</span>
    <span>22</span><span>23</span><span>24</span><span>25</span><span>26</span><span>27</span><span>28</span>
    <span>29</span><span>30</span><span>31</span>
  </div></section>

  <section class="month green" style="left:313px;top:589px;height:146px"><div class="month-name">AUGUST</div><div class="days">
    <span class="hd">S</span><span class="hd">M</span><span class="hd">T</span><span class="hd">W</span><span class="hd">T</span><span class="hd">F</span><span class="hd">S</span>
    <span></span><span></span><span></span><span>1</span><span>2</span><span>3</span><span>4</span>
    <span>5</span><span>6</span><span>7</span><span>8</span><span>9</span><span>10</span><span>11</span>
    <span>12</span><span>13</span><span>14</span><span>15</span><span>16</span><span>17</span><span>18</span>
    <span>19</span><span>20</span><span>21</span><span>22</span><span>23</span><span>24</span><span>25</span>
    <span>26</span><span>27</span><span>28</span><span>29</span><span>30</span><span>31</span>
  </div></section>

  <section class="month green" style="left:591px;top:589px;height:146px"><div class="month-name">SEPTEMBER</div><div class="days">
    <span class="hd">S</span><span class="hd">M</span><span class="hd">T</span><span class="hd">W</span><span class="hd">T</span><span class="hd">F</span><span class="hd">S</span>
    <span>30</span><span></span><span></span><span></span><span></span><span></span><span>1</span>
    <span>2</span><span>3</span><span>4</span><span>5</span><span>6</span><span>7</span><span>8</span>
    <span>9</span><span>10</span><span>11</span><span>12</span><span>13</span><span>14</span><span>15</span>
    <span>16</span><span>17</span><span>18</span><span>19</span><span>20</span><span>21</span><span>22</span>
    <span>23</span><span class="hol">24</span><span>25</span><span>26</span><span>27</span><span>28</span><span>29</span>
  </div></section>

  <section class="month yellow" style="left:35px;top:742px;height:145px"><div class="month-name">OCTOBER</div><div class="days">
    <span class="hd">S</span><span class="hd">M</span><span class="hd">T</span><span class="hd">W</span><span class="hd">T</span><span class="hd">F</span><span class="hd">S</span>
    <span></span><span>1</span><span>2</span><span>3</span><span>4</span><span>5</span><span>6</span>
    <span>7</span><span>8</span><span>9</span><span>10</span><span>11</span><span>12</span><span>13</span>
    <span>14</span><span>15</span><span>16</span><span>17</span><span>18</span><span>19</span><span>20</span>
    <span>21</span><span>22</span><span>23</span><span>24</span><span>25</span><span>26</span><span>27</span>
    <span>28</span><span>29</span><span>30</span><span>31</span>
  </div></section>

  <section class="month yellow" style="left:313px;top:742px;height:145px"><div class="month-name">NOVEMBER</div><div class="days">
    <span class="hd">S</span><span class="hd">M</span><span class="hd">T</span><span class="hd">W</span><span class="hd">T</span><span class="hd">F</span><span class="hd">S</span>
    <span></span><span></span><span></span><span></span><span>1</span><span>2</span><span>3</span>
    <span>4</span><span>5</span><span>6</span><span>7</span><span>8</span><span>9</span><span>10</span>
    <span>11</span><span>12</span><span>13</span><span>14</span><span>15</span><span>16</span><span>17</span>
    <span>18</span><span>19</span><span>20</span><span>21</span><span>22</span><span>23</span><span>24</span>
    <span>25</span><span>26</span><span>27</span><span>28</span><span>29</span><span>30</span>
  </div></section>

  <section class="month yellow" style="left:591px;top:742px;height:145px"><div class="month-name">DECEMBER</div><div class="days">
    <span class="hd">S</span><span class="hd">M</span><span class="hd">T</span><span class="hd">W</span><span class="hd">T</span><span class="hd">F</span><span class="hd">S</span>
    <span>30</span><span>31</span><span></span><span></span><span></span><span></span><span>1</span>
    <span>2</span><span>3</span><span>4</span><span>5</span><span>6</span><span>7</span><span>8</span>
    <span>9</span><span>10</span><span>11</span><span>12</span><span>13</span><span>14</span><span>15</span>
    <span>16</span><span>17</span><span>18</span><span>19</span><span>20</span><span>21</span><span>22</span>
    <span>23</span><span>24</span><span class="hol">25</span><span class="hol">26</span><span>27</span><span>28</span><span>29</span>
  </div></section>

  <div class="legend">
    <span class="key"><span class="swatch" style="background:var(--m-yellow)"></span>Harvesting</span>
    <span class="key"><span class="swatch" style="background:var(--m-brown)"></span>Sowing</span>
    <span class="key"><span class="swatch" style="background:var(--m-green)"></span>Growing</span>
    <span class="key"><span class="swatch" style="background:#fff"></span>Liming + Fertilising</span>
  </div>

  <footer>
    <div class="footer-left"></div>
    <div class="footer-right"></div>
    <div class="contact" style="left:58px;top:927px">
      <svg width="14" height="14" viewBox="0 0 14 14"><circle cx="7" cy="7" r="7" fill="#fff"/><path d="M7 3a2.5 2.5 0 0 0-2.5 2.5C4.5 7.5 7 11 7 11s2.5-3.5 2.5-5.5A2.5 2.5 0 0 0 7 3z" fill="var(--brand-green)"/></svg>
      <span>42 Mill Road,<br>Tarrawong NSW 2700, Australia</span>
    </div>
    <div class="contact" style="left:254px;top:929px">
      <svg width="14" height="14" viewBox="0 0 14 14"><circle cx="7" cy="7" r="7" fill="#fff"/><path d="M4.5 3.5l1.5-.3 1 2-1 .8c.4 1 1.1 1.7 2 2.1l.8-1 2 1-.3 1.5c-3.3.2-6.2-2.7-6-6.1z" fill="var(--brand-green)"/></svg>
      <span>02-5550-0142</span>
    </div>
    <div class="contact" style="left:513px;top:929px">
      <svg width="14" height="14" viewBox="0 0 14 14"><circle cx="7" cy="7" r="6.3" fill="none" stroke="#fff" stroke-width="1.2"/><ellipse cx="7" cy="7" rx="2.6" ry="6.3" fill="none" stroke="#fff" stroke-width="1"/><path d="M1 7h12" stroke="#fff" stroke-width="1"/></svg>
      <span>www.brevardholdings.com.au</span>
    </div>
  </footer>
</main>
</body>
</html>
```